Modern, upmarket label design for food product

We need a label design for a food company producing nuts with sesame and honey. In fact, we would like the words "Cashews med sesam & honning" on the label (It's in Danish and means - Cashews with sesame & honey). It should be easy for the customer to quickly understand what it is.

It is a shelf product in the competitive food industry, which is why the design should wake the feeling of 'just wanting to grab the product down from the shelves'. So, the design should stand out and have an image of a cool, modern, hip product. This being said, I love a raw & handmade look.

The company is called Tyvo. Its origins are from the danish word Pilt that is a Danish slang for yummy. I have uploaded a photo of the package the products will be sold in.

Info & dimensions on bag in picture 1.
Dimensions: 6" x 9" | 15.2 cm x 22.3 cm
Capacity: 8 ounces | 250 grams (based on whole bean coffee)

Picture 2 is the same product, but has the possibility of attaching to a hanger on shelfs.

Picture 3 - I have also uploaded a photo of a product bag, where the hole is linear instead of a round hole. The designer chooses, which bag they will like to work with!

Please let me know if there are any questions!

Target Market(s)

Target market could really be any age, but the design needs to compel the target audience to pick it from the shelves. The package should signal a product you want to hold and have other people seeing you have it. The target audience is people who cares for what they buy, and typically doesn't want a low-end or budget product. They want the whole thing, meaning it has to taste good, look good etc. They are also the type of people who like to show off whatever products they buy by placing them in their houses for their guests to see. Or by uploading pictures of it on social medias.

Industry/Entity Type

It Company

Font styles to use
Other font styles liked:
• Not a must, but I like the 'Panton' script

Requirements
Must have
• My project must have the words 'Cashews med sesam & honning' on the label, so the customer will know within a second what they are looking at and buying.
Nice to have
• I am picturing the label with the words 'Cashews med sesam & honning' as a statement, again, emphasizing how the customer instantly should know what the product is. This being said, it should not be the only thing on the package and I love a raw & handmade look - which inspiration picture 5 is a great example of!
• I have uploaded photos of what I think looks good. With this said, I am not looking for a copy of those products, but see them as good inspiration. I have named the photos inspiration 1, 2, 3, 4 & 5.
• If needed, more text can be put on the label. For example 'vegan', 'laktosefri', Glutenfri', or 'Sund Snack' are great words for being used on the label.
Should not have
• The fonts on the label should not be too decorative. Personally I like an easy too read font.

```html
<!DOCTYPE html>
<html lang="da">
<head>
<meta charset="utf-8">
<title>Tyvo – cashews med sesam &amp; honning</title>
<link rel="stylesheet" href="https://fonts.googleapis.com/css2?family=Jost:wght@300;400&display=swap">
<style>
  :root {
    --page: #ffffff;
    --kraft: #bf987c;
    --window: #ede2da;
    --seam: #e4d4c7;
    --type-light: #ffffff;
    --type-dark: #1e1a18;
    --shadow: rgba(0, 0, 0, 0.18);
  }
  html, body {
    margin: 0;
    width: 1200px;
    height: 922px;
    overflow: hidden;
    background: var(--page);
  }
  .canvas {
    position: relative;
    width: 1200px;
    height: 922px;
  }
  .label {
    position: absolute;
    left: 337px;
    top: 83px;
    width: 526px;
    height: 755px;
    filter: drop-shadow(1px 2px 2px var(--shadow));
  }
  .label-body { fill: var(--kraft); }
  .label-seam { stroke: var(--seam); stroke-width: 1; }
  .label-window { fill: var(--window); }
  .product-name {
    font-family: "Jost", "Futura", sans-serif;
    font-weight: 300;
    font-size: 92px;
    fill: var(--type-light);
  }
  .product-name .ampersand { fill: var(--type-dark); }
  .brand-name {
    font-family: "Jost", "Futura", sans-serif;
    font-weight: 400;
    font-size: 28px;
    fill: var(--type-light);
  }
  .net-weight {
    font-family: "Jost", "Futura", sans-serif;
    font-weight: 400;
    font-size: 18px;
    fill: var(--type-light);
  }
  .net-weight-divider { stroke: var(--type-dark); stroke-width: 1.5; }
</style>
</head>
<body>
<main class="canvas">
  <svg class="label" viewBox="0 0 526 755" width="526" height="755" role="img" aria-label="Tyvo label: cashews med sesam &amp; honning, 8 ounces, 250 grams">
    <rect class="label-body" x="0" y="0" width="526" height="755"/>
    <line class="label-seam" x1="0" y1="73" x2="526" y2="73"/>

    <text class="product-name">
      <tspan x="86" y="180">cashews</tspan>
      <tspan x="426" y="230" text-anchor="end">med</tspan>
      <tspan x="113" y="280">sesam</tspan>
      <tspan class="ampersand" x="331" y="320">&amp;</tspan>
      <tspan x="93" y="368">honning</tspan>
    </text>

    <ellipse class="label-window" cx="256" cy="523" rx="168" ry="92"/>

    <text class="brand-name" x="256" y="680" text-anchor="middle">Tyvo</text>

    <text class="net-weight" x="238" y="713" text-anchor="end">8 ounces</text>
    <line class="net-weight-divider" x1="252" y1="695" x2="252" y2="722"/>
    <text class="net-weight" x="265" y="713">250 grams</text>
  </svg>
</main>
</body>
</html>
```